DL Cards to get buyers attention

I’m looking to have four double-sided DL flyers professionally prepared and made print-ready in high resolution.

I have uploaded the four existing designs, and I’m happy for them to be reviewed with a fresh set of eyes. While I’m generally happy with the direction, I’m very open to recommendations around layout, typography, imagery, colour balance, spacing and overall presentation if there are opportunities to create a stronger and more professional result.

The key objective is to develop a consistent and recognisable suite of marketing material that strengthens both Jen Callow brand awareness and my personal profile in the local real estate market. Each flyer should feel like part of the same campaign while still having its own clear message and purpose.

I want the finished designs to feel professional, confident, modern and premium, without becoming overly busy or losing the simplicity that makes a DL flyer easy to read. Strong headlines, clear messaging and an obvious call to action are important. The Jen Callow branding should be immediately recognisable, while my photograph, name and contact details should be incorporated naturally and consistently.

Please review the existing designs and suggest any changes that would improve their visual impact, readability and consistency. I’m also open to seeing an alternative design direction if you believe there is a better overall look.

The final artwork needs to be supplied professionally print-ready at DL size (210 mm × 99 mm), double-sided, high resolution, CMYK where appropriate, with 3 mm bleed and safe margins, so it can be provided directly to a commercial printer.

The overall goal is simple: strong branding, professional presentation, consistent recognition and marketing material that people will remember.

Target Market(s)

People looking at selling their homes

Industry/Entity Type

Real Estate

Font styles to use
Serif
Sans Serif

Requirements
Must have
• Strong brand awareness - Jen Callow
Nice to have
• bright and fresh

```html
<!DOCTYPE html>
<html lang="en">
<head>
<meta charset="utf-8">
<title>Jen Callow DL Flyer Suite</title>
<link href="https://fonts.googleapis.com/css2?family=Montserrat:ital,wght@0,400;0,500;0,600;0,700;0,800;1,500;1,700&family=Mrs+Saint+Delafield&display=swap" rel="stylesheet">
<style>
:root{
  --board:#3b3c3c;
  --yellow:#ffe512;
  --ink:#111111;
  --white:#ffffff;
  --bar:#3f4040;
  --sans:'Montserrat', Arial, sans-serif;
  --script:'Mrs Saint Delafield', cursive;
}
*{box-sizing:border-box;margin:0;padding:0}
html,body{width:1200px;height:2323px;overflow:hidden;background:var(--board);font-family:var(--sans);color:var(--ink)}
.flyer{position:absolute;left:61px;width:1077px;height:507px;background:var(--white);overflow:hidden}
.flyer--keys{top:84px}
.flyer--checklist{top:633px}
.flyer--steps{top:1182px}
.flyer--process{top:1732px}

.panel-yellow{position:absolute;left:0;top:0;width:468px;height:507px;background:var(--yellow)}
.photo{position:absolute}
.brand-box{position:absolute;background:var(--yellow);display:flex;align-items:center;justify-content:center}
.brand-name{font-family:var(--sans);font-weight:800;color:var(--ink);letter-spacing:-0.5px;white-space:nowrap}
.brand-box--large{left:746px;top:0;width:245px;height:244px}
.brand-box--large .brand-name{font-size:38px;margin-top:60px}
.brand-box--small{left:910px;top:0;width:115px;height:115px}
.brand-box--small .brand-name{font-size:18px;margin-top:28px}

.headline{position:absolute;left:51px;font-weight:800;line-height:0.9;text-transform:uppercase;letter-spacing:-0.5px}
.keys-title{top:68px;font-size:58px}
.keys-title span{display:block}
.script-band{position:absolute;left:0;top:232px;width:468px;height:120px;background:var(--ink);color:var(--white);font-family:var(--script);font-size:74px;line-height:124px;padding-left:58px;white-space:nowrap;overflow:hidden}
.lede{position:absolute;left:75px;font-size:22px;font-weight:500;line-height:1.0}
.keys-lede{top:382px;width:320px}

.tip{position:absolute;width:175px}
.tip-head{display:flex;gap:6px;align-items:flex-start;font-weight:700;font-size:11px;line-height:1.1;text-transform:uppercase}
.tip-head svg{flex:none}
.tip p{font-size:9.5px;line-height:1.05;margin-top:10px;padding-left:5px;width:135px}
.motto{position:absolute;left:405px;top:258px;font-family:var(--script);color:var(--yellow);font-size:62px;line-height:0.95;transform:rotate(-6deg)}
.call-bar{position:absolute;left:39px;top:400px;width:1000px;height:107px;background:var(--bar);display:flex;align-items:center;color:var(--white);font-weight:800}
.call-bar .call{font-size:55px;margin-left:47px;letter-spacing:0.5px}
.call-bar .ring{margin-left:36px}
.call-bar .num{font-size:55px;margin-left:28px;letter-spacing:0.5px}

.steps-title{top:58px;font-size:50px}
.steps-script{position:absolute;left:62px;top:150px;font-family:var(--script);font-size:165px;line-height:165px;color:var(--ink);white-space:nowrap}
.steps-lede{top:372px;width:300px}

.stage{position:absolute;top:56px}
.stage-head{display:flex;align-items:center;gap:8px}
.stage-no{font-size:26px;font-weight:700;color:var(--yellow)}
.stage-title{font-size:12px;font-weight:700;line-height:1.05;text-transform:uppercase;white-space:nowrap}
.stage-item{position:absolute;width:140px}
.stage-item h4{font-size:11.5px;font-weight:700;line-height:1.05}
.stage-item p{font-size:9.2px;line-height:1.05;margin-top:2px}
.stage-tip{position:absolute;width:160px;display:flex;gap:4px;font-size:9px;font-style:italic;line-height:1.08}
.stage-tip svg{flex:none;margin-top:-4px}
.stage-rule{position:absolute;top:476px;width:66px;height:2px;background:var(--yellow)}

.values{position:absolute;left:729px;top:101px;list-style:none}
.values li{display:flex;align-items:center;gap:10px;font-size:11px;font-weight:700;height:26px;text-transform:uppercase}
.invite{position:absolute;left:722px;top:191px;width:345px;height:106px;background:var(--yellow);padding:19px 0 0 19px;font-size:13px;font-weight:700;font-style:italic;line-height:1.05}
.invite span{display:block;width:150px}
.reach{position:absolute;left:732px;top:312px;font-family:var(--script);font-size:40px;line-height:0.85;transform:rotate(-6deg)}
.agent-sign{position:absolute;left:720px;top:382px;font-family:var(--script);font-size:40px;line-height:40px;color:var(--yellow)}
.contact{position:absolute;left:722px;top:436px;display:flex;align-items:center;gap:8px;font-size:37px;font-weight:800}
</style>
</head>
<body>

<section class="flyer flyer--keys">
  <div class="photo" role="img" aria-label="Photo of a hand passing house keys over a model house and contract" style="left:468px;top:0;width:583px;height:507px;background:linear-gradient(160deg,#f4f4f2 0%,#e4e1dc 55%,#d7cfc4 100%)"></div>
  <div class="panel-yellow"></div>
  <h1 class="headline keys-title"><span>10 Things</span><span>to get your</span><span>property</span></h1>
  <div class="script-band">Ready to Sell</div>
  <p class="lede keys-lede">A well-prepared home makes a lasting first impression and helps achieve the best result.</p>
  <div class="brand-box brand-box--large"><span class="brand-name">Jen Callow</span></div>
</section>

<section class="flyer flyer--checklist">
  <div class="photo" role="img" aria-label="Portrait photo of agent Mark in a white shirt" style="left:720px;top:20px;width:357px;height:380px;background:linear-gradient(90deg,#ffffff 0%,#f4f1ec 45%,#ece9e5 100%)"></div>
  <div class="tip" style="left:45px;top:55px">
    <div class="tip-head"><svg width="26" height="26" viewBox="0 0 26 26"><path d="M13 2l2.5 8.5L24 13l-8.5 2.5L13 24l-2.5-8.5L2 13l8.5-2.5z" fill="none" stroke="var(--yellow)" stroke-width="2"/></svg><span>Clean &amp;<br>Declutter</span></div>
    <p>Remove personal items and clutter. A clean, tidy home feels bigger, brighter and more inviting.</p>
  </div>
  <div class="tip" style="left:223px;top:55px">
    <div class="tip-head"><svg width="26" height="26" viewBox="0 0 26 26"><path d="M4 22L22 4M4 4l18 18" stroke="var(--yellow)" stroke-width="2.5"/></svg><span>Finish projects<br>&amp; repairs</span></div>
    <p>Fix minor issues, leaky taps, loose handles and any repairs buyers will notice.</p>
  </div>
  <div class="tip" style="left:392px;top:55px">
    <div class="tip-head"><svg width="26" height="26" viewBox="0 0 26 26"><circle cx="13" cy="13" r="11" fill="none" stroke="var(--yellow)" stroke-width="2"/><path d="M8 13l4 4 7-8" fill="none" stroke="var(--yellow)" stroke-width="2"/></svg><span>Do a thorough<br>inspection</span></div>
    <p>Check the big and small things - inside and out - so there are no surprises later.</p>
  </div>
  <div class="tip" style="left:579px;top:55px">
    <div class="tip-head"><svg width="26" height="26" viewBox="0 0 26 26"><rect x="3" y="3" width="18" height="7" fill="none" stroke="var(--yellow)" stroke-width="2"/><path d="M21 7h3v6H12v4M12 17v7" fill="none" stroke="var(--yellow)" stroke-width="2"/></svg><span>Paint</span></div>
    <p>A fresh coat of neutral paint can transform your home and make it feel well maintained.</p>
  </div>

  <div class="tip" style="left:45px;top:165px">
    <div class="tip-head"><svg width="26" height="26" viewBox="0 0 26 26"><circle cx="13" cy="12" r="7" fill="none" stroke="var(--yellow)" stroke-width="2"/><path d="M10 20h6M11 24h4" stroke="var(--yellow)" stroke-width="2"/></svg><span>Freshen up fixtures<br>&amp; hardware</span></div>
    <p>Update old light fittings, tapware and cabinet handles for an instant lift.</p>
  </div>
  <div class="tip" style="left:223px;top:165px">
    <div class="tip-head"><svg width="26" height="26" viewBox="0 0 26 26"><path d="M13 3l10 5-10 5-10-5zM3 13l10 5 10-5M3 18l10 5 10-5" fill="none" stroke="var(--yellow)" stroke-width="2"/></svg><span>Clean or replace<br>flooring</span></div>
    <p>Clean carpets, tiles and floors or replace if needed. Great floors make a big difference.</p>
  </div>
  <div class="tip" style="left:392px;top:165px">
    <div class="tip-head"><svg width="26" height="26" viewBox="0 0 26 26"><rect x="6" y="2" width="14" height="22" fill="none" stroke="var(--yellow)" stroke-width="2"/><circle cx="16" cy="13" r="1.3" fill="var(--yellow)"/></svg><span>Create a welcoming<br>entrance</span></div>
    <p>Tidy up the front yard, clean the entry and add plants for great street appeal.</p>
  </div>
  <div class="tip" style="left:579px;top:165px">
    <div class="tip-head"><svg width="26" height="26" viewBox="0 0 26 26"><path d="M3 20V10h20v10M3 15h20M5 20v3M21 20v3" fill="none" stroke="var(--yellow)" stroke-width="2"/></svg><span>Stage your<br>home</span></div>
    <p>Arrange furniture to showcase space and lifestyle. Less is more when selling.</p>
  </div>

  <div class="tip" style="left:45px;top:275px">
    <div class="tip-head"><svg width="26" height="26" viewBox="0 0 26 26"><circle cx="13" cy="15" r="9" fill="none" stroke="var(--yellow)" stroke-width="2"/><path d="M10 6c0-3 6-3 6 0" fill="none" stroke="var(--yellow)" stroke-width="2"/></svg><span>Eliminate<br>odours</span></div>
    <p>Remove pet smells, smoke, cooking and musty odours for a fresh, neutral home.</p>
  </div>
  <div class="tip" style="left:223px;top:275px">
    <div class="tip-head"><svg width="26" height="26" viewBox="0 0 26 26"><text x="7" y="21" font-family="Montserrat, sans-serif" font-size="22" font-weight="700" fill="none" stroke="var(--yellow)" stroke-width="1.3">$</text></svg><span>Get your<br>real price</span></div>
    <p>Work with an agent to set the right price and attract the right buyers.</p>
  </div>

  <div class="motto">Your Property<br>&nbsp;Our Priority</div>
  <div class="brand-box brand-box--small"><span class="brand-name">Jen Callow</span></div>
  <div class="call-bar">
    <span class="call">CALL MARK</span>
    <svg class="ring" width="70" height="70" viewBox="0 0 70 70"><circle cx="35" cy="35" r="35" fill="var(--yellow)"/><path d="M25 20c-3 2-4 6-2 11 3 7 9 14 16 17 5 2 8 1 10-2l-5-6-4 2c-3-1-7-5-8-8l2-4z" fill="var(--bar)"/></svg>
    <span class="num">0491 57 01 10</span>
  </div>
</section>

<section class="flyer flyer--steps">
  <div class="photo" role="img" aria-label="Photo of a starfish standing on a sunny beach with the ocean behind" style="left:468px;top:0;width:583px;height:507px;background:linear-gradient(180deg,#9fcbe0 0%,#5fa9c6 22%,#d9e8ec 38%,#e9d9c2 55%,#dcc6a8 100%)"></div>
  <div class="panel-yellow"></div>
  <h2 class="headline steps-title">Steps of a</h2>
  <div class="steps-script">Sale</div>
  <p class="lede steps-lede">A clear process. Proven results. From listing to settlement, I'm with you every step of the way.</p>
  <div class="brand-box brand-box--large"><span class="brand-name">Jen Callow</span></div>
</section>

<section class="flyer flyer--process">
  <div class="photo" role="img" aria-label="Portrait photo of agent Mark in a white shirt" style="left:892px;top:125px;width:185px;height:382px;background:linear-gradient(180deg,#f3efea 0%,#ece7e1 55%,#f5f5f5 100%)"></div>

  <div class="stage" style="left:41px">
    <div class="stage-head"><span class="stage-no">01</span><span class="stage-title">Preparation<br>&amp; appraisal</span></div>
  </div>
  <div class="stage-item" style="left:50px;top:113px"><h4>Agent selection</h4><p>Choose a local agent and set a realistic selling price based on market research.</p></div>
  <div class="stage-item" style="left:50px;top:186px"><h4>Home styling</h4><p>Clean, declutter, and repair flaws to make the property photogenic. You can read Seven important tips for a successful sale from Jen Callow for guidance on staging your home.</p></div>
  <div class="stage-item" style="left:50px;top:300px"><h4>Contract<br>preparation</h4><p>Work with a solicitor or conveyancer to prepare the contract of sale and vendor statement.</p></div>
  <div class="stage-tip" style="left:38px;top:426px"><svg width="14" height="14" viewBox="0 0 14 14"><circle cx="7" cy="7" r="4" fill="var(--yellow)"/></svg><span>Good preparation can make a big difference to how buyers see your property.</span></div>
  <div class="stage-rule" style="left:50px"></div>

  <div class="stage" style="left:210px">
    <div class="stage-head"><span class="stage-no">02</span><span class="stage-title">Choosing a<br>method of sale</span></div>
  </div>
  <div class="stage-item" style="left:225px;top:113px"><h4>Auction</h4><p>Set a date, market without a price to build urgency, and encourage competitive bidding</p></div>
  <div class="stage-item" style="left:225px;top:211px"><h4>Private Treaty</h4><p>List an asking price and negotiate individual offers with buyers.</p></div>
  <div class="stage-item" style="left:225px;top:300px"><h4>Expressions of<br>Interest / Tender</h4><p>Invite confidential offers by a set date for unique properties.</p></div>
  <div class="stage-tip" style="left:203px;top:398px"><svg width="14" height="14" viewBox="0 0 14 14"><circle cx="7" cy="7" r="4" fill="var(--yellow)"/></svg><span>The right method of sale depends on your property, the local market and your goals. Your agent can recommend the strategy best suited to achieving a strong result.</span></div>
  <div class="stage-rule" style="left:220px"></div>

  <div class="stage" style="left:389px">
    <div class="stage-head"><span class="stage-no">03</span><span class="stage-title">Marketing<br>&amp; campaign</span></div>
  </div>
  <div class="stage-item" style="left:398px;top:113px"><h4>Launch your<br>campaign</h4><p>Present your property to the market with professional photography, online advertising, signage and targeted promotion.</p></div>
  <div class="stage-item" style="left:398px;top:209px"><h4>Inspections</h4><p>Hold open homes and private viewings to give prospective buyers the opportunity to experience your property.</p></div>
  <div class="stage-item" style="left:398px;top:300px"><h4>Vendor reports</h4><p>Receive regular updates from your agent covering buyer feedback, inspection numbers, enquiry levels and overall market interest.</p></div>
  <div class="stage-tip" style="left:381px;top:426px"><svg width="14" height="14" viewBox="0 0 14 14"><circle cx="7" cy="7" r="4" fill="var(--yellow)"/></svg><span>A strong marketing campaign creates exposure, builds buyer interest and helps generate competition for your property.</span></div>
  <div class="stage-rule" style="left:398px"></div>

  <div class="stage" style="left:563px">
    <div class="stage-head"><span class="stage-no">04</span><span class="stage-title">Contract exchange<br>&amp; settlement</span></div>
  </div>
  <div class="stage-item" style="left:572px;top:113px"><h4>Exchange</h4><p>Both buyer and seller sign separate copies of the contract, and they are swapped.</p></div>
  <div class="stage-item" style="left:572px;top:186px"><h4>Deposit</h4><p>The buyer pays a deposit (usually 10%), which is held in a trust account.</p></div>
  <div class="stage-item" style="left:572px;top:253px"><h4>Cooling-off</h4><p>Private treaty sales usually include a 5-day cooling-off period for buyers (none at auction).</p></div>
  <div class="stage-item" style="left:572px;top:330px"><h4>Settlement</h4><p>The final transaction is completed, typically 42 days (six weeks) after exchange, and keys are handed over.</p></div>
  <div class="stage-tip" style="left:555px;top:412px"><svg width="14" height="14" viewBox="0 0 14 14"><circle cx="7" cy="7" r="4" fill="var(--yellow)"/></svg><span>Your agent, solicitor or conveyancer will guide you through the final steps from exchange through to settlement and key handover.</span></div>
  <div class="stage-rule" style="left:572px"></div>

  <ul class="values">
    <li><svg width="18" height="18" viewBox="0 0 18 18"><path d="M9 1L1 8h2v9h4v-5h4v5h4V8h2z" fill="var(--ink)"/></svg>Local knowledge</li>
    <li><svg width="18" height="18" viewBox="0 0 18 18"><circle cx="9" cy="9" r="7.5" fill="none" stroke="var(--ink)" stroke-width="2"/><path d="M9 13L5.5 9.5a2 2 0 013.5-2.5 2 2 0 013.5 2.5z" fill="var(--ink)"/></svg>Exceptional service</li>
    <li><svg width="18" height="18" viewBox="0 0 18 18"><path d="M9 16L2 9a4 4 0 017-5 4 4 0 017 5z" fill="#e02020"/></svg>Genuine care</li>
  </ul>
  <div class="invite"><span>If you are thinking of selling, planning to sell or would simply like to chat about your options ..</span></div>
  <div class="brand-box brand-box--small"><span class="brand-name">Jen Callow</span></div>
  <div class="reach">Reach out and<br>&nbsp;call me today.</div>
  <div class="agent-sign">MARK</div>
  <div class="contact">
    <svg width="48" height="48" viewBox="0 0 70 70"><circle cx="35" cy="35" r="35" fill="var(--yellow)"/><path d="M25 20c-3 2-4 6-2 11 3 7 9 14 16 17 5 2 8 1 10-2l-5-6-4 2c-3-1-7-5-8-8l2-4z" fill="var(--white)"/></svg>
    <span>0491 57 01 10</span>
  </div>
</section>

</body>
</html>
```